High-End Medical Center Website Design Project

This design is part of a well thought-out project by an experienced project manager / developer. The approved wireframe is attached. Creative interpretations / suggestions based on the layout encouraged.

The design is for a new state-of-the-art medical center located in Dallas, Texas. The target audience would likely be individuals (approx. 60% female /40% male) who are the healthcare decision-makers for their families. They would likely have insurance and be inclined to seek out top-quality care.

Potential clients would choose this client over others in their industry because the medical center is physician owned, meaning it is patient-focused rather than profit-focused. The facility is brand new, featuring the latest technology. (This includes an amazing waiting room featuring WiFi and docking stations.) The physicians are hand-picked by referral only.

The look of the site should be extremely clean. We are going for a well-organized, professional look with a bit of a warm glow (interpret that however you like). Use crisp corners and the colors in the logo.

Think modern, clean with some great use of color / font.

We can get lovely photography of the medical center once construction is complete. Feel free to use an "example image" behind the Featured Area ("Physician Owned. Patient-Focused") if you like. We are open to ideas.

ONE CHANGE REQUESTED IN THE WIREFRAME:

Remove the "Connect" 1/4 page footer area and replace with a quick contact form. You may swap the "Locations" area with the form if desired. Put social media icons at the top left of the page in the top header area.

(Note: Please use social media icons that match the design rather than standard icons. We preferred not placing the icons at the top, but the client requested this. Let's not bring more attention to them than necessary.)
Updates

We're custom programming this site, so there's no need to base it on a template. Also, we would prefer not to use typical "seen everywhere" stock images.Thanks.

Industry/Entity Type

Construction

Requirements
Must have
• Follow the wireframe. This has been approved.
Nice to have
• Examples of what hover states, links or dropdowns might look like.

```html
<!DOCTYPE html>
<html lang="en">
<head>
<meta charset="utf-8">
<title>Nova Medical Center</title>
<link href="https://fonts.googleapis.com/css2?family=Open+Sans:wght@400;600;700&family=Arimo:wght@400;700&display=swap" rel="stylesheet">
<style>
:root{
  --blue:#0b54a2;
  --blue-dark:#0a3d73;
  --blue-soft:#3d7bbf;
  --mist:#eef6f6;
  --ink:#222;
  --text:#3a3a3a;
  --muted:#777;
  --teal:#6aa9a4;
  --pale:#cfe0f2;
  --line:#d8d8d8;
  --placeholder:#c3ccd3;
  --head:"Open Sans",sans-serif;
  --body:"Arimo",Arial,sans-serif;
}
*{margin:0;padding:0;box-sizing:border-box}
html,body{width:823px;height:1200px;overflow:hidden;background:#fff}
body{position:relative;font-family:var(--body);color:var(--text);font-size:8.5px}
a{color:inherit;text-decoration:none}
.abs{position:absolute}

.top{left:0;top:0;width:823px;height:64px;background:#f6f6f6}
.brand{left:77px;top:18px;display:flex;align-items:center;gap:6px}
.brand-mark{width:22px;height:22px;background:var(--blue)}
.brand-name{font-family:var(--head);font-weight:700;font-size:17px;color:var(--blue);letter-spacing:.3px}
.phone{right:71px;top:20px;font-weight:700;font-size:11px;color:var(--blue)}
.social{display:flex;gap:2px}
.social span{width:16px;height:16px;display:block}
.social .s1{background:#2b2b2b}.social .s2{background:#3b5998}.social .s3{background:#c4302b}.social .s4{background:#33aadd}
.social-top{right:71px;top:39px}

.nav{left:0;top:64px;width:823px;height:39px;background:#fff;border-top:1px solid #e8e8e8}
.nav ul{list-style:none;display:flex;position:absolute;left:66px;top:0;height:39px}
.nav li{font-weight:700;font-size:8px;color:#333;padding:0 14px;line-height:39px;border-right:1px solid #ececec}
.nav li:hover{color:var(--blue)}

.feature{left:0;top:103px;width:823px;height:465px;background:var(--blue)}
.slide{left:66px;top:19px;width:686px;height:290px;background:linear-gradient(180deg,#e6eef4 0%,#c9dbeb 55%,#7fa7cf 100%)}
.dots{left:380px;display:flex;gap:6px}
.dots span{width:13px;height:13px;border-radius:50%;background:#ddd;border:1px solid #bbb}
.dots .on{background:#2aa0b8;border:3px solid #ddd}
.tagline{left:0;top:323px;width:823px;text-align:center;font-family:var(--head);font-weight:600;font-size:15.5px;color:var(--pale)}
.point{top:353px;width:150px;text-align:center;color:#e5eef8;font-size:8.2px;line-height:11.5px}
.point svg{display:block;margin:0 auto 10px}
.point b{color:#fff}

.apart{left:0;top:568px;width:823px;height:184px}
.apart h2{position:absolute;left:0;width:823px;top:16px;text-align:center;font-family:var(--head);font-weight:600;font-size:15px;color:#111}
.apart .rule{left:321px;top:38px;width:199px;height:1px;background:var(--blue-soft)}
.merit{top:62px;width:190px;text-align:center;font-size:8.2px;line-height:12px;color:#333}
.merit h3{font-family:var(--head);font-weight:600;font-size:12px;color:var(--blue-soft);margin-bottom:12px}
.merit a{color:var(--blue-soft);font-weight:700}
.merit .dotted{margin-top:8px;border-top:1px dotted #aaa}

.info{left:0;top:752px;width:823px;height:210px;background:var(--mist)}
.info h2{font-family:var(--head);font-weight:600;font-size:12px;color:#111}
.hospital-img{left:88px;top:34px;width:157px;height:103px;background:var(--placeholder)}
.about-text{left:262px;top:34px;width:258px;font-size:8.2px;line-height:13.6px;color:#333}
.about-text a{display:block;color:#555;margin-top:2px}
.portrait{left:546px;top:41px;width:62px;height:64px;background:#e3cdb9}
.quote{left:618px;top:38px;width:135px;font-size:8.2px;line-height:13.6px;color:#333}
.quote2{left:549px;top:123px;width:200px;font-size:8.2px;line-height:13.6px;color:#333}
.who{left:550px;top:159px;font-size:8px;line-height:14px;color:var(--muted)}
.who b{color:#555}

.footer{left:0;top:962px;width:823px;height:179px;background:var(--blue);color:#dbe7f4;font-size:8.2px;line-height:11px}
.footer h4{font-family:var(--head);font-weight:700;font-size:9.5px;line-height:11px;color:#fff;margin-bottom:17px}
.col{top:17px}
.news p{margin-bottom:12px}.news b{color:#e6eef8}
.blog p{margin-bottom:13px;width:115px}
.form h4{margin-bottom:18px}
.form label{display:block;color:#fff;font-weight:700;font-size:7px;line-height:8px}
.form .field{width:98px;height:18px;background:#fff;border:1px solid #ccc;margin-bottom:8px}
.form .msg{height:31px;margin-bottom:3px}
.submit{width:47px;height:17px;background:var(--teal);color:#fff;font-size:8px;text-align:center;line-height:17px;margin-left:1px}
.submit:hover{background:#5a958f}
.loc p{margin-bottom:14px;width:118px}
.wait{left:638px;width:118px;text-align:center}
.wait h4{margin-bottom:15px}
.wait .count{width:45px;height:38px;margin:0 auto;background:#fff;color:var(--blue);font-size:24px;line-height:38px;font-family:var(--body)}
.wait .unit{font-size:11px;line-height:14px;color:#fff;margin:2px 0 3px}

.base{left:0;top:1141px;width:823px;height:59px}
.copy{left:82px;top:16px;font-size:8px;line-height:10px;color:#999}
.social-foot{left:651px;top:12px;align-items:center}
.social-foot em{font-style:normal;font-size:8px;color:#333;margin-left:6px}
</style>
</head>
<body>

<header class="abs top">
  <div class="abs brand"><span class="brand-mark"></span><span class="brand-name">NOVA MEDICAL CENTER</span></div>
  <div class="abs phone">Call us Now: (555) 014 2290</div>
  <div class="abs social social-top"><span class="s1"></span><span class="s2"></span><span class="s3"></span><span class="s4"></span></div>
</header>

<nav class="abs nav">
  <ul><li>HOME</li><li>WHY NOVA</li><li>PHYCISIANS</li><li>SPECIALITIES</li><li>INFO</li><li>LOCATIONS</li><li>CONTACT</li></ul>
</nav>

<section class="abs feature">
  <div class="abs slide" role="img" aria-label="Photo of four smiling physicians in white coats and scrubs"></div>
  <div class="abs dots" style="top:282px;left:316px"><span></span><span></span><span class="on"></span><span></span><span></span></div>
  <div class="abs tagline">PHYSICIAN OWNED. PATIENT FOCUSED</div>

  <div class="abs point" style="left:83px">
    <svg width="44" height="44" viewBox="0 0 44 44"><rect x="3" y="3" width="38" height="38" rx="5" fill="none" stroke="var(--blue-dark)" stroke-width="5"/><path d="M22 12v20M12 22h20" stroke="var(--blue-dark)" stroke-width="5"/></svg>
    Sed ut perspiciatis unde omnis iste natus error sit voluptatem accusantium doloremque<br><b>Read more..</b>
  </div>
  <div class="abs point" style="left:342px">
    <svg width="44" height="44" viewBox="0 0 44 44"><rect x="3" y="3" width="38" height="38" rx="5" fill="none" stroke="var(--blue-dark)" stroke-width="5"/><path d="M12 13h20M12 19h14M12 25h18M12 31h10" stroke="var(--blue-dark)" stroke-width="3"/></svg>
    Sed ut perspiciatis unde omnis iste natus error sit voluptatem accusantium doloremque<br><b>Read more..</b>
  </div>
  <div class="abs point" style="left:583px">
    <svg width="44" height="44" viewBox="0 0 44 44"><path d="M10 22a14 14 0 1 0 4-10" fill="none" stroke="var(--blue-dark)" stroke-width="5"/><path d="M4 12l11-2-3 11z" fill="var(--blue-dark)"/><path d="M23 14v9h7" fill="none" stroke="var(--blue-dark)" stroke-width="4"/></svg>
    Sed ut perspiciatis unde omnis iste natus error sit voluptatem accusantium doloremque<br><b>Read more..</b>
  </div>
</section>

<section class="abs apart">
  <h2>WHAT SETS US APART</h2>
  <div class="abs rule"></div>
  <div class="abs merit" style="left:70px"><h3>TECHNOLOGY</h3>Etiam at risus et justo dignissim congue. Donec congue lacinia dui, a porttitor lectus condimentum laoreet. Nunc eu ullamcorper orci. Quisque eget odio.<br><a href="#">Read more..</a><div class="dotted"></div></div>
  <div class="abs merit" style="left:319px"><h3>QUALITY OF CARE</h3>Etiam at risus et justo dignissim congue. Donec congue lacinia dui, a porttitor lectus condimentum laoreet. Nunc eu ullamcorper orci. Quisque eget odio.<br><a href="#">Read more..</a><div class="dotted" style="margin-top:17px"></div></div>
  <div class="abs merit" style="left:564px"><h3>PATIENT EXPERIENCE</h3>Etiam at risus et justo dignissim congue. Donec congue lacinia dui, a porttitor lectus condimentum laoreet. Nunc eu ullamcorper orci. Quisque eget odio.<br><a href="#">Read more..</a><div class="dotted"></div></div>
</section>

<section class="abs info">
  <h2 class="abs" style="left:89px;top:12px">ABOUT OUR HOSPITAL</h2>
  <div class="abs hospital-img" role="img" aria-label="Photo of the hospital building"></div>
  <div class="abs about-text">Sed ut perspiciatis unde omnis iste natus error sit voluptatem dolorem que laudantium, totam rem eaque ipsa quae ab illo inveeritatis et quasi architecto beatae vitae dicta sunt explicabo. Nevoluptatem quia voluptas sit aspernatur aut odit aut fugit, sed qu uuntur magni dolores eos qui rationvoluptatem sequi nesciunt. &nbsp;voluptatem quia voluptas sit aspernatur aut odit aut fugit, sed uuntur magni dolores eos qui rationvoluptatem sequi nesciunt.<a href="#">Read more..</a></div>

  <h2 class="abs" style="left:544px;top:12px">TESTIMONIALS</h2>
  <div class="abs portrait" role="img" aria-label="Photo of a mother and her adult daughter"></div>
  <div class="abs quote">Sed ut perspiciatis unde omnis iste natus error sit voluptatem dolorem que laudantium, totam rem eaque ipsa quae ab illo inve eritatis et quasi architecto</div>
  <div class="abs quote2">Sed ut perspiciatis unde omnis iste natus error sit doloremque laudantium</div>
  <div class="abs who">Mother &amp; Daughter<br><b>Laura Bennett</b></div>
</section>

<footer class="abs footer">
  <div class="abs col news" style="left:78px"><h4>NEWS</h4>
    <p><b>20-07-2013</b><br>Sed ut perspiciatis unde omnis<br>sit voluptatem dolorem que</p>
    <p><b>20-07-2013</b><br>Sed ut perspiciatis unde omnis<br>sit voluptatem dolorem</p>
    <p><b>20-07-2013</b><br>Sed ut perspiciatis unde omnis<br>sit voluptatem dolorem</p>
  </div>
  <div class="abs col blog" style="left:217px"><h4>BLOG</h4>
    <p style="margin-top:10px">Sed ut perspiciatis unde omnis sit voluptatem dolorem</p>
    <p style="margin-top:24px">Sed ut perspiciatis unde omnis sit voluptatem dolorem</p>
    <p style="margin-top:20px">Sed ut perspiciatis unde omnis sit voluptatem dolorem</p>
  </div>
  <div class="abs col form" style="left:372px"><h4>CONNECT</h4>
    <label>Name</label><div class="field"></div>
    <label>Email</label><div class="field"></div>
    <label>Message</label><div class="field msg"></div>
    <div class="submit">SUBMIT</div>
  </div>
  <div class="abs col loc" style="left:493px"><h4 style="margin-bottom:20px">LOCATIONS</h4>
    <p>ADDRESS 1<br>Sed ut perspiciatis unde omnis sit voluptatem dolorem</p>
    <p>ADDRESS 2<br>Sed ut perspiciatis unde omnis sit voluptatem dolorem</p>
  </div>
  <div class="abs col wait"><h4>AVERAGE WAITING TIME</h4>
    <div class="count">09</div>
    <div class="unit">Mintues</div>
    Sed ut perspiciatis unde<br>omnis sit voluptatem<br>dolorem
  </div>
</footer>

<div class="abs base">
  <div class="abs copy">Copyright 2013. All rights reserved.<br>Terms &amp; Conditions &nbsp;- &nbsp;&nbsp;Privacy &nbsp;&nbsp;- &nbsp;&nbsp;Disclaimer</div>
  <div class="abs social social-foot"><span class="s1"></span><span class="s2"></span><span class="s3"></span><span class="s4"></span><em>X5</em></div>
</div>

</body>
</html>
```